Media Kit

We're a editorial website that enjoys some love from advertisers and publicists.
We need a digital media kit (probably in PDF form) that tells a story about who we are, who our readers are, our traffic and so forth.
The copy and a logo file are attached - you just need to make it look awesome. Our logo font is 'elephant'. Our secondary font is Futura Lt Bt.
To get a sense of the types of media kits in the market, check out:
http://www.novapresskit.example/hotdata/publishers/novapk/advertiser/4471902/5530617/MediaKitFinal_2013.pdf
http://www.bluelantern84.example/static/corporate/images/3f912a/corporate/assets/bl84_mediakit.pdf
Or look to other traditional and digital magazines in the lifestyle space.
Please note: we will require the original artwork files from the successful designer.
Updates
If you wish, a sample rather than the whole project is fine to secure payment.
Target Market(s)
Publicists, Marketing Managers, Media Buyers
Industry/Entity Type
Digital
Look and feel
Each slider illustrates characteristics of the customer's brand and the style your logo design should communicate.

```html
<!DOCTYPE html>
<html lang="en">
<head>
<meta charset="utf-8">
<title>The Velvet Lane – Media Kit</title>
<link href="https://fonts.googleapis.com/css2?family=Abril+Fatface&family=Jost:wght@300;400;500&display=swap" rel="stylesheet">
<style>
:root{
  --canvas:#e4e4e4;
  --page:#ffffff;
  --page-shade:#cfcfcf;
  --ink:#111111;
  --ink-soft:#3a3a3a;
  --muted:#a3a3a3;
  --chart-light:#bdbdbd;
  --crowd:#c9c9c9;
  --photo-light:#ece9e5;
  --photo-mid:#b9aa98;
}
*{box-sizing:border-box;margin:0;padding:0}
html,body{width:1200px;height:1000px;overflow:hidden}
body{background:var(--canvas);font-family:'Jost',sans-serif;font-weight:300;color:var(--ink);position:relative}
.page{position:absolute;background:linear-gradient(100deg,var(--page) 40%,var(--page-shade) 100%);box-shadow:0 2px 10px rgba(0,0,0,.18);overflow:hidden}
.spread-left{left:30px;top:30px;width:565px;height:450px;background:linear-gradient(90deg,var(--page) 45%,var(--page-shade) 100%)}
.spread-right{left:605px;top:30px;width:565px;height:450px;background:linear-gradient(90deg,#d9d9d9 0%,var(--page) 35%,#e2e2e2 100%)}
.cover{left:60px;top:510px;width:480px;height:340px;background:var(--page)}
.back{left:640px;top:510px;width:480px;height:340px}

.brand{position:absolute;display:flex;align-items:center;gap:6px;font-family:'Jost',sans-serif;font-weight:500;font-size:10px;color:var(--ink);letter-spacing:.02em}
.brand-dot{width:26px;height:26px;border-radius:50%;background:var(--ink)}

.heading{font-family:'Abril Fatface',serif;font-weight:400;color:var(--ink);line-height:1}
.copy{position:absolute;font-size:7.5px;color:var(--muted);line-height:1.35}
.copy p{margin-bottom:9px}
.copy b{font-weight:400;color:var(--ink);font-size:11px}

/* who are we */
.who{left:205px;top:28px;width:340px}
.who .heading{font-size:22px;margin-bottom:12px}
.vision{position:absolute;left:22px;top:330px;width:150px}
.vision .heading{font-size:18px;margin-bottom:6px}
.vision-line{font-size:14px;color:var(--muted);line-height:1.1;display:flex;justify-content:space-between}
.vision-line.dark{color:var(--ink-soft)}
.vision-line.spaced{letter-spacing:.12em}
.vision-line.wide{letter-spacing:.5em;font-size:8px;line-height:1.4}

/* the picture */
.picture-title{position:absolute;left:230px;top:80px}
.picture-title .heading{font-size:22px}
.picture-intro{position:absolute;left:230px;top:112px;width:300px;font-size:7.5px;color:var(--muted);line-height:1.5}
.picture-intro b{font-weight:400;color:var(--ink);font-size:12px}
.crowd{position:absolute;left:18px;top:170px;width:140px;height:140px}
.stat-label{font-size:8px;color:var(--ink-soft);text-align:center}
.clock{position:absolute;left:178px;top:196px;width:150px}
.laptop{position:absolute;left:350px;top:168px;width:190px}
.returns{position:absolute;left:130px;top:330px;display:flex;align-items:center;gap:14px}
.returns-text{font-size:9px;line-height:1.15;text-align:center}
.returns-text .big{font-size:22px;display:block}
.returns-text .mid{font-size:13px;display:block}
.donut{position:absolute;left:330px;top:306px;width:130px;height:130px}

/* cover */
.cover-photo{position:absolute;inset:0;background:radial-gradient(ellipse at 50% 55%,var(--photo-mid) 0%,var(--photo-light) 60%,#f4f3f1 100%)}
.cover-label{position:absolute;left:140px;top:218px;width:200px;height:44px;background:rgba(255,255,255,.92);display:flex;align-items:center;gap:8px;padding:0 10px}
.cover-label .brand-dot{width:30px;height:30px}
.cover-label-text{line-height:1.05}
.cover-label-name{font-size:12px;color:var(--muted);letter-spacing:.04em}
.cover-label-kit{font-size:16px;font-weight:500;color:var(--ink);text-align:right}

/* back */
.back-block{position:absolute;left:190px;width:270px}
.back-block .heading{font-size:15px;margin-bottom:4px}
.back-note{font-size:6.5px;color:var(--muted);margin-bottom:6px}
.network-cols{display:grid;grid-template-columns:1fr 1fr;font-size:9px;color:var(--muted);line-height:1.25}
.year-list{font-size:6.5px;color:var(--muted);line-height:1.3}
.year-list p{margin-bottom:5px}
.year-list b{font-weight:400;color:var(--ink);font-size:9px}
.contact{position:absolute;left:26px;top:245px;font-size:8px;color:var(--ink-soft);line-height:1.25}
.contact .heading{font-size:15px;margin-bottom:6px;color:var(--ink)}
.contact-sub{margin-bottom:10px}
</style>
</head>
<body>

<section class="page spread-left">
  <div class="brand" style="left:20px;top:22px"><span class="brand-dot"></span>the velvet lane</div>
  <div class="copy who">
    <h2 class="heading">Who Are We?</h2>
    <p>The Velvet Lane is all about the <b>lovely things in life</b></p>
    <p>It is the home for <b>delectable fashion</b>, <b>enviable interiors</b>, <b>inspired music</b> and <b>memorable travel experiences</b> to name just a few.</p>
    <p>Most of all however, it's about these things being <b>accessible to everyone</b></p>
    <p>That means that as <b>beautiful as the photos look</b>, we know most people can't really live with all white interiors. Or walk down the street wearing a nude tulle skirt.</p>
    <p>That said, there's <b>no reason practicality means boring or ugly</b></p>
    <p>Of course, like real lives, wardrobes, diets and MP3 players, at <b>The Velvet Lane Solvane</b> lives happily alongside Marrow &amp; Co, you'll see superfoods as well as sundaes and hear Dolly Verve on the same playlist as Rocky Frost.</p>
    <p>The Velvet Lane is based in Melbourne, Australia and takes submissions and <b>content from all over the world</b></p>
    <p>With everything we do we always consider the fact that we live in an age where <b>people see</b>, <b>read</b>, <b>hear</b> and <b>experience things</b> that might be happening in the next street or on the other side of the world.</p>
    <p>This means that everything that appears in The Velvet Lane is <b>meaningful</b> no matter where you <b>live</b>, <b>work</b> and <b>play</b></p>
  </div>
  <div class="vision">
    <h2 class="heading">Our Vision</h2>
    <div class="vision-line"><span>The</span><span>home</span><span>of</span></div>
    <div class="vision-line dark spaced"><span>accessible</span></div>
    <div class="vision-line dark"><span>inspiring</span><span style="color:var(--muted)">and</span></div>
    <div class="vision-line wide"><span>beautiful</span></div>
    <div class="vision-line"><span style="color:var(--ink-soft)">lifestyle</span><span>elements.</span></div>
  </div>
</section>

<section class="page spread-right">
  <div class="brand" style="left:18px;top:22px"><span class="brand-dot"></span>the velvet lane</div>
  <div class="picture-title"><h2 class="heading">The Picture</h2></div>
  <p class="picture-intro">The Velvet Lane is very young, but we're <b>growing up fast</b><br>Our <b>readership</b> and reach <b>expands every day</b></p>

  <svg class="crowd" viewBox="0 0 140 140" role="img" aria-label="Circle filled with a crowd of reader figures">
    <circle cx="70" cy="70" r="68" fill="var(--crowd)"/>
    <circle cx="70" cy="62" r="36" fill="var(--ink)"/>
    <text x="70" y="48" text-anchor="middle" fill="#fff" font-family="Jost" font-size="8">Up to</text>
    <text x="70" y="64" text-anchor="middle" fill="#fff" font-family="Jost" font-size="15">3,500</text>
    <text x="70" y="75" text-anchor="middle" fill="#fff" font-family="Jost" font-size="7">unique visitors</text>
    <text x="70" y="84" text-anchor="middle" fill="#fff" font-family="Jost" font-size="7">each day</text>
  </svg>

  <div class="clock">
    <div class="stat-label">Average time on site</div>
    <svg viewBox="0 0 150 80" width="150" height="80">
      <rect x="2" y="4" width="146" height="72" rx="10" fill="var(--ink)"/>
      <rect x="10" y="12" width="130" height="56" rx="4" fill="#fff"/>
      <text x="75" y="56" text-anchor="middle" font-family="Jost" font-size="40" fill="var(--ink)" letter-spacing="2">04:30</text>
    </svg>
  </div>

  <div class="laptop">
    <svg viewBox="0 0 190 130" width="190" height="130">
      <rect x="22" y="4" width="146" height="104" rx="8" fill="var(--ink)"/>
      <rect x="32" y="14" width="126" height="86" rx="3" fill="#fff"/>
      <rect x="4" y="110" width="182" height="10" rx="3" fill="var(--ink)"/>
      <text x="95" y="42" text-anchor="middle" font-family="Jost" font-size="9" fill="#333">Average pages per visit</text>
      <text x="95" y="76" text-anchor="middle" font-family="Jost" font-size="24" fill="var(--ink)">7.3</text>
    </svg>
  </div>

  <div class="returns">
    <svg viewBox="0 0 56 56" width="56" height="56">
      <circle cx="28" cy="28" r="27" fill="var(--ink)"/>
      <path d="M14 23h16v-8l14 13-14 13v-8H14z" fill="#fff"/>
    </svg>
    <div class="returns-text"><span class="big">38%</span>of readers<br>come back<span class="mid">3 or more times</span>a month</div>
  </div>

  <svg class="donut" viewBox="0 0 130 130">
    <circle cx="65" cy="65" r="52" fill="none" stroke="var(--ink)" stroke-width="20"/>
    <path d="M65 13 A52 52 0 0 1 114 83" fill="none" stroke="var(--chart-light)" stroke-width="20"/>
    <text x="65" y="58" text-anchor="middle" font-family="Jost" font-size="7" fill="var(--ink)">More than half</text>
    <text x="65" y="68" text-anchor="middle" font-family="Jost" font-size="7" fill="var(--ink)">our traffic is made up</text>
    <text x="65" y="78" text-anchor="middle" font-family="Jost" font-size="7" fill="var(--ink)">of first time visitors</text>
  </svg>
</section>

<section class="page cover">
  <div class="cover-photo" role="img" aria-label="Group of five stylish friends posing together against a pale studio backdrop"></div>
  <div class="cover-label">
    <span class="brand-dot"></span>
    <div class="cover-label-text">
      <div class="cover-label-name">the velvet lane</div>
      <div class="cover-label-kit">media kit</div>
    </div>
  </div>
</section>

<section class="page back">
  <div class="brand" style="left:18px;top:20px"><span class="brand-dot"></span>the velvet lane</div>
  <div class="back-block" style="top:22px">
    <h2 class="heading">Our Network</h2>
    <p class="back-note">Some of our current and previous advertisers and affiliate partners include:</p>
    <div class="network-cols">
      <span>The Sellroom</span><span>Ritual Glow</span>
      <span>Our Closet</span><span>Ashcombe</span>
      <span>Pairings Style</span><span>Milo Hartwell</span>
    </div>
  </div>
  <div class="back-block" style="top:100px">
    <h2 class="heading">The Year Ahead</h2>
    <div class="year-list">
      <p>Establishment of contributor network to have <b>daily updates</b> in each major category.</p>
      <p>Launch our <b>weekly newsletter</b></p>
      <p>Develop <b>custom visual content.</b></p>
    </div>
  </div>
  <div class="contact">
    <h2 class="heading">Contact</h2>
    <p class="contact-sub">Press Releases &amp; Other Media Enquiries</p>
    <p>Clara Whitlow</p>
    <p>clara@thevelvetlane.example</p>
    <p>+61 (0) 400 555 017</p>
    <p>www.thevelvetlane.example</p>
  </div>
</section>

</body>
</html>
```